The Reefside Clinic PowerPoint Design

We are looking for a new PowerPoint template design to reflect our branding and to be used for presentations at international conferences and online conferences. An example of our current template which is outdated is attached. We would like to still have a blue colour background as this represents water (but the exact background can be modified). We would like a professional, modern, and sharp feel to the templates. The template should include an Intro Slide, content slide, and closing/questions slide. The template needs to be prepared for both the standards, the 4:3 and Wide screen 16:9. Logos and branding in the attached power point can be used. Please visit our website www.thereefsideclinic.com to see more about the company.

```html
<!DOCTYPE html>
<html lang="en">
<head>
<meta charset="utf-8">
<title>The Reefside Clinic – Presentation Template</title>
<link href="https://fonts.googleapis.com/css2?family=Roboto:wght@300;400;700&family=Roboto+Condensed:wght@400&display=swap" rel="stylesheet">
<style>
:root{
  --navy:#0d2062;
  --page:#ffffff;
  --blue-1:#2f6db4;
  --blue-2:#3b82c8;
  --blue-3:#4a9ad6;
  --blue-4:#6fb3e2;
  --blue-pale:#c8d9ec;
  --sky:#56b4e9;
  --text:#ffffff;
  --muted:#8fa3cf;
  --link:#3c7fd6;
  --badge:#6aa832;
}
*{box-sizing:border-box;margin:0;padding:0}
html,body{width:900px;height:1200px;overflow:hidden;background:var(--page)}
.sheet{position:relative;width:900px;height:1200px}
.slide{position:absolute;width:302px;height:170px;background:var(--navy);overflow:hidden;color:var(--text);
  font-family:"Roboto",sans-serif;box-shadow:4px 6px 14px rgba(0,0,0,.22)}
.col-a{left:103px}.col-b{left:494px}
.row-1{top:22px}.row-2{top:220px}.row-3{top:418px}.row-4{top:616px}.row-5{top:815px}.row-6{top:1013px}
.abs{position:absolute}
.title{position:absolute;left:23px;top:15px;font-weight:400;font-size:13.5px;letter-spacing:.1px;line-height:1}
.subtitle{position:absolute;left:23px;top:33px;font-size:3.3px;color:var(--muted);letter-spacing:.1px;text-transform:uppercase}
.brand{position:absolute;right:24px;top:22px;font-family:"Roboto",sans-serif;font-weight:700;font-size:4.4px;color:var(--text);display:flex;align-items:center;gap:2px}
.brand .dot{width:3px;height:3px;border-radius:50%;background:var(--sky)}
.footer{position:absolute;left:22px;bottom:4px;font-size:2.8px;color:var(--muted)}
.footer span{color:var(--link)}
.page-no{position:absolute;right:24px;bottom:4px;font-size:2.8px;color:var(--muted)}
.photo{position:absolute}
.ph-fish{background:linear-gradient(135deg,#c9c89a,#3b4fc4 45%,#e9e6d8 70%,#b7a56a)}
.ph-water{background:linear-gradient(180deg,#2a8fd0,#0f5496)}
.ph-shark{background:radial-gradient(ellipse at 55% 60%,#3d6b7e,#1a78b8 60%,#0f5a99)}
.ph-ray{background:radial-gradient(ellipse at 50% 45%,#5b8ea8,#1e86cc 60%,#126fb3)}
.ph-whale{background:linear-gradient(160deg,#6fa3c4,#cfd8df 45%,#8aa5b8 75%,#2c6b9e)}
.ph-discus{background:linear-gradient(160deg,#3d6a3a,#5a5e8a 50%,#253f5a)}
.ph-coral{background:linear-gradient(135deg,#e0c9a0,#b5402e 45%,#6b2a22)}
.ph-turtle{background:linear-gradient(180deg,#1ea5df,#23b6d9 55%,#7a9e6a)}
.ph-reef{background:linear-gradient(180deg,#1f9ad8,#1570b2 60%,#d86a2a)}
.ph-penguin{background:linear-gradient(180deg,#34bfcf,#8fc8b8 45%,#1c2b2a 60%,#e4d9a2)}
.ph-seahorse{background:radial-gradient(ellipse at 40% 50%,#e0a040,#8a5a2c 55%,#d7c7a8)}
.ph-jelly{background:radial-gradient(ellipse at 45% 40%,#f08a2a,#b04a1a 35%,#1d4fd0 70%)}
.ph-egg{background:radial-gradient(ellipse at 35% 45%,#f2a11c,#6a2a08 40%,#c9b7a4 70%,#e8e2dc)}
.ph-diver{background:linear-gradient(160deg,#2a5a7a,#0f2236 60%,#3a6e90)}
.ph-vet{background:linear-gradient(160deg,#3a4b5c,#c9d3dc 60%,#f0f2f4)}
.ph-seaturtle{background:linear-gradient(150deg,#3e5a4a,#6b7a52 45%,#2f4a45)}
/* title slide */
.intro-photo{left:0;top:0;width:302px;height:112px}
.badge{position:absolute;right:5px;top:104px;width:49px;height:15px;background:var(--badge)}
.intro-title{position:absolute;left:0;right:0;top:124px;text-align:center;font-family:"Roboto Condensed",sans-serif;font-size:11px}
.intro-author{position:absolute;left:0;right:0;top:138px;text-align:center;font-family:"Roboto Condensed",sans-serif;font-size:5px}
.intro-desc{position:absolute;left:30px;right:30px;top:145px;text-align:center;font-family:"Roboto Condensed",sans-serif;font-size:3.5px;line-height:1.45}
.intro-slide .brand{top:16px;right:20px}
/* team */
.team-card{position:absolute;height:45px;width:83px;padding:4px 6px}
.team-card h3{font-family:"Roboto Condensed",sans-serif;font-weight:400;font-size:5.6px;margin-bottom:1px}
.team-card .cred{font-size:2.7px;line-height:1.3;margin-bottom:2px;font-family:"Roboto Condensed",sans-serif}
.team-card p{font-size:3px;line-height:1.5}
.team-card b{font-weight:700}
/* vision */
.service{position:absolute;width:126px;height:46px;border-radius:12px;background:var(--blue-2);overflow:hidden}
.service .photo{left:0;top:0;width:50px;height:46px;border-radius:12px 0 0 12px}
.service h3{position:absolute;left:63px;top:9px;font-family:"Roboto Condensed",sans-serif;font-weight:400;font-size:5.8px}
.service p{position:absolute;left:63px;top:19px;width:56px;font-size:3.3px;line-height:1.55}
/* generic text cells */
.cell{position:absolute;padding:8px 6px}
.cell h3{font-family:"Roboto Condensed",sans-serif;font-weight:400;font-size:5.3px}
.cell .rule{width:7px;height:.5px;background:currentColor;margin:3px 0 3px;opacity:.8}
.cell p{font-size:3.1px;line-height:1.55}
.cell b{font-weight:700}
.tone-1{background:var(--blue-1)}
.tone-2{background:var(--blue-2)}
.tone-3{background:var(--blue-3)}
.tone-4{background:var(--blue-4)}
.tone-pale{background:var(--blue-pale)}
.body-text{position:absolute;font-size:3.1px;line-height:1.65}
.body-text b{font-weight:700}
.hline{position:absolute;height:.5px;background:#4b62a6}
.big-title{position:absolute;left:23px;font-weight:400;line-height:.95}
</style>
</head>
<body>
<div class="sheet">

<!-- 1 intro -->
<section class="slide col-a row-1 intro-slide">
  <div class="photo ph-fish intro-photo" role="img" aria-label="Photo of a clown triggerfish with white spots on a blue body"></div>
  <div class="brand">The Reefside Clinic<i class="dot"></i></div>
  <div class="badge"></div>
  <h1 class="intro-title">Module One - Fish Anatomy and Physiology</h1>
  <div class="intro-author">Dr Ruth Jarvis</div>
  <p class="intro-desc">Examines teleost anatomy in its wide forms as well as practical physiology. To understand how fish survive in an aquatic environment is critical to maintaining their health and wellbeing. Normal anatomy is critical for diagnostics and post-mortems</p>
  <div class="footer">The Reefside Clinic presentation to: <span>Harbourview Marine Park</span></div>
  <div class="page-no">Page: 1</div>
</section>

<!-- 2 team -->
<section class="slide col-b row-1">
  <h2 class="title">OUR TEAM</h2>
  <div class="subtitle">Lorem ipsum, giving information on its origins, as well as a random text here</div>
  <div class="brand">The Reefside Clinic<i class="dot"></i></div>
  <div class="photo ph-diver" style="left:23px;top:49px;width:45px;height:45px" role="img" aria-label="Portrait photo of Dr Ruth Jarvis in a wetsuit"></div>
  <div class="team-card tone-1" style="left:68px;top:49px"><h3>Dr Ruth Jarvis</h3><div class="cred">BVSc (Hons), Aquatic Animal Health, Aquaculture Manager</div><p><b>Lorem Ipsum</b> is simply dummy text of the printing and typesetting industry. Lorem Ipsum has been the industry's standard.</p></div>
  <div class="photo ph-diver" style="left:151px;top:49px;width:45px;height:45px" role="img" aria-label="Portrait photo of Dr Ben Dalton holding a sea turtle"></div>
  <div class="team-card tone-2" style="left:196px;top:49px"><h3>Dr Ben Dalton</h3><div class="cred">Bachelor of Science in Biology, Coastal University</div><p><b>Lorem Ipsum</b> is simply dummy text of the printing and typesetting industry. Lorem Ipsum has been the industry's standard.</p></div>
  <div class="team-card tone-3" style="left:23px;top:99px"><h3>Dr Liam Rourke</h3><div class="cred">Marine Biology degree, Southern University</div><p><b>Lorem Ipsum</b> is simply dummy text of the printing and typesetting industry. Lorem Ipsum has been the industry's standard.</p></div>
  <div class="photo ph-shark" style="left:106px;top:99px;width:45px;height:45px" role="img" aria-label="Portrait photo of Dr Liam Rourke at an aquarium"></div>
  <div class="team-card tone-4" style="left:151px;top:99px"><h3>Dr. Marco Gallo</h3><div class="cred">Bachelor of Science, First Class Honours</div><p><b>Lorem Ipsum</b> is simply dummy text of the printing and typesetting industry. Lorem Ipsum has been the industry's standard.</p></div>
  <div class="photo ph-vet" style="left:234px;top:99px;width:45px;height:45px" role="img" aria-label="Portrait photo of Dr. Marco Gallo with a dog"></div>
  <div class="footer">The Reefside Clinic presentation to: <span>Harbourview Marine Park</span></div>
  <div class="page-no">Page: 2</div>
</section>

<!-- 3 vision -->
<section class="slide col-a row-2">
  <h2 class="title">OUR VISION</h2>
  <div class="subtitle">To advance the health and welfare of aquatic animals in aquariums and zoos globally</div>
  <div class="brand">The Reefside Clinic<i class="dot"></i></div>
  <div class="service" style="left:23px;top:49px"><div class="photo ph-penguin" role="img" aria-label="Photo of a penguin swimming underwater"></div><h3>Consultation</h3><p><b>Lorem Ipsum</b> is simply dummy text of the printing and typesetting industry. Lorem Ipsum has been.</p></div>
  <div class="service" style="left:153px;top:49px"><div class="photo ph-seahorse" role="img" aria-label="Photo of a seahorse"></div><h3>Education</h3><p><b>Lorem Ipsum</b> is simply dummy text of the printing and typesetting industry. Lorem Ipsum has been.</p></div>
  <div class="service" style="left:23px;top:102px"><div class="photo ph-fish" role="img" aria-label="Photo of a clown triggerfish"></div><h3>Conferences</h3><p><b>Lorem Ipsum</b> is simply dummy text of the printing and typesetting industry. Lorem Ipsum has been.</p></div>
  <div class="service" style="left:153px;top:102px"><div class="photo ph-jelly" role="img" aria-label="Photo of an orange jellyfish"></div><h3>Reproduction</h3><p><b>Lorem Ipsum</b> is simply dummy text of the printing and typesetting industry. Lorem Ipsum has been.</p></div>
  <div class="footer">The Reefside Clinic presentation to: <span>Harbourview Marine Park</span></div>
  <div class="page-no">Page: 3</div>
</section>

<!-- 4 content -->
<section class="slide col-b row-2">
  <h2 class="title">CONTENT SLIDE</h2>
  <div class="subtitle">Lorem ipsum, giving information on its origins, as well as a random text here</div>
  <div class="brand">The Reefside Clinic<i class="dot"></i></div>
  <div class="footer">The Reefside Clinic presentation to: <span>Harbourview Marine Park</span></div>
  <div class="page-no">Page: 4</div>
</section>

<!-- 5 text with image -->
<section class="slide col-a row-3">
  <h2 class="title">TEXT WITH IMAGE</h2>
  <div class="subtitle" style="width:125px;line-height:1.2">Lorem ipsum, giving information on its origins, as well as a random text here</div>
  <div class="body-text" style="left:23px;top:58px;width:125px">
    <p><b>Lorem Ipsum</b> is simply dummy text of the printing and typesetting industry. Lorem Ipsum has been the industry's standard dummy text ever since the 1500s, when an unknown printer took a galley of type and scrambled it to make a type specimen book. It has survived not only five centuries but also the leap into electronic typesetting, remaining essentially unchanged.</p><br>
    <p>Lorem Ipsum is simply dummy text of the printing and typesetting industry. Lorem Ipsum has been the industry's standard dummy text ever since the 1500s, when an unknown printer took a galley of type and scrambled it to make a type specimen book. It has survived not only five centuries but also the leap into electronic typesetting, remaining essentially unchanged.</p>
  </div>
  <div class="photo ph-egg" style="left:168px;top:0;width:134px;height:170px" role="img" aria-label="Photo of hands holding a backlit shark egg case"></div>
  <div class="footer">The Reefside Clinic presentation to: <span>Harbourview Marine Park</span></div>
</section>

<!-- 6 portfolio -->
<section class="slide col-b row-3">
  <h2 class="title">PORTAFOLIO OPTIONS</h2>
  <div class="subtitle">Lorem ipsum, giving information on its origins, as well as a random text here</div>
  <div class="brand">The Reefside Clinic<i class="dot"></i></div>
  <div class="photo ph-discus" style="left:23px;top:46px;width:69px;height:99px" role="img" aria-label="Photo of discus fish among aquarium plants"></div>
  <div class="photo ph-shark" style="left:93px;top:46px;width:69px;height:51px" role="img" aria-label="Photo of a shark swimming"></div>
  <div class="cell tone-2" style="left:93px;top:98px;width:69px;height:47px;padding:6px 5px"><h3>Content Text here</h3><div class="rule"></div><p><b>Lorem Ipsum</b> is simply dummy text of the printing and typesetting industry. Lorem Ipsum has been the industry's.</p></div>
  <div class="photo ph-ray" style="left:163px;top:46px;width:116px;height:51px" role="img" aria-label="Photo of an eagle ray swimming"></div>
  <div class="photo ph-whale" style="left:163px;top:98px;width:116px;height:47px" role="img" aria-label="Photo of a whale shark close up"></div>
  <div class="footer">The Reefside Clinic presentation to: <span>Harbourview Marine Park</span></div>
  <div class="page-no">Page: 6</div>
</section>

<!-- 7 portfolio grid -->
<section class="slide col-a row-4">
  <h2 class="title">PORTAFOLIO OPTIONS</h2>
  <div class="subtitle">Lorem ipsum, giving information on its origins, as well as a random text here</div>
  <div class="brand">The Reefside Clinic<i class="dot"></i></div>
  <div class="photo ph-fish" style="left:0;top:49px;width:50px;height:50px" role="img" aria-label="Photo of a clown triggerfish"></div>
  <div class="cell tone-1" style="left:50px;top:49px;width:50px;height:50px;padding:6px 5px"><h3>Content Text</h3><div class="rule"></div><p><b>Lorem Ipsum</b> is simply dummy text of the printing and typesetting industry.</p></div>
  <div class="photo ph-discus" style="left:100px;top:49px;width:51px;height:50px" role="img" aria-label="Photo of discus fish"></div>
  <div class="cell tone-pale" style="left:151px;top:49px;width:50px;height:50px;padding:6px 5px;color:#eef4fb"><h3>Content Text</h3><div class="rule"></div><p><b>Lorem Ipsum</b> is simply dummy text of the printing and typesetting industry.</p></div>
  <div class="photo ph-shark" style="left:201px;top:49px;width:50px;height:50px" role="img" aria-label="Photo of a shark"></div>
  <div class="cell tone-3" style="left:251px;top:49px;width:51px;height:50px;padding:6px 5px"><h3>Content Text</h3><div class="rule"></div><p><b>Lorem Ipsum</b> is simply dummy text of the printing and typesetting industry.</p></div>
  <div class="cell tone-1" style="left:0;top:99px;width:50px;height:51px;padding:6px 5px"><h3>Content Text</h3><div class="rule"></div><p><b>Lorem Ipsum</b> is simply dummy text of the printing and typesetting industry.</p></div>
  <div class="photo ph-whale" style="left:50px;top:99px;width:50px;height:51px" role="img" aria-label="Photo of a whale shark"></div>
  <div class="cell tone-4" style="left:100px;top:99px;width:51px;height:51px;padding:6px 5px"><h3>Content Text</h3><div class="rule"></div><p><b>Lorem Ipsum</b> is simply dummy text of the printing and typesetting industry.</p></div>
  <div class="photo ph-turtle" style="left:151px;top:99px;width:50px;height:51px" role="img" aria-label="Photo of a sea turtle"></div>
  <div class="cell tone-3" style="left:201px;top:99px;width:50px;height:51px;padding:6px 5px;background:var(--sky)"><h3>Content Text</h3><div class="rule"></div><p><b>Lorem Ipsum</b> is simply dummy text of the printing and typesetting industry.</p></div>
  <div class="photo ph-reef" style="left:251px;top:99px;width:51px;height:51px" role="img" aria-label="Photo of reef fish schooling"></div>
  <div class="footer">The Reefside Clinic presentation to: <span>Harbourview Marine Park</span></div>
  <div class="page-no">Page: 7</div>
</section>

<!-- 8 portfolio big -->
<section class="slide col-b row-4">
  <h2 class="title">PORTAFOLIO OPTIONS</h2>
  <div class="subtitle">Lorem ipsum, giving information on its origins, as well as a random text here</div>
  <div class="brand">The Reefside Clinic<i class="dot"></i></div>
  <div class="photo ph-shark" style="left:0;top:49px;width:151px;height:101px" role="img" aria-label="Photo of a shark in an aquarium tank"></div>
  <div class="cell tone-pale" style="left:151px;top:49px;width:50px;height:50px;padding:6px 5px;color:#eef4fb"><h3>Texto</h3><div class="rule"></div><p><b>Lorem Ipsum</b> is simply dummy text of the printing and typesetting industry.</p></div>
  <div class="photo ph-whale" style="left:201px;top:49px;width:51px;height:50px" role="img" aria-label="Photo of a whale shark"></div>
  <div class="cell" style="left:252px;top:49px;width:50px;height:50px;padding:6px 5px;background:var(--sky)"><h3>Texto</h3><div class="rule"></div><p><b>Lorem Ipsum</b> is simply dummy text of the printing and typesetting industry.</p></div>
  <div class="photo ph-ray" style="left:151px;top:99px;width:50px;height:51px" role="img" aria-label="Photo of an eagle ray"></div>
  <div class="cell" style="left:201px;top:99px;width:51px;height:51px;padding:6px 5px;background:#8ccbe8"><h3>Texto</h3><div class="rule"></div><p><b>Lorem Ipsum</b> is simply dummy text of the printing and typesetting industry.</p></div>
  <div class="photo ph-coral" style="left:252px;top:99px;width:50px;height:51px" role="img" aria-label="Photo of a red coral fish"></div>
  <div class="footer">The Reefside Clinic presentation to: <span>Harbourview Marine Park</span></div>
  <div class="page-no">Page: 8</div>
</section>

<!-- 9 text with two images -->
<section class="slide col-a row-5">
  <h2 class="title">TEXT WITH TWO IMAGES</h2>
  <div class="subtitle">Lorem ipsum, giving information on its origins, as well as a random text here</div>
  <div class="brand">The Reefside Clinic<i class="dot"></i></div>
  <div class="photo ph-shark" style="left:23px;top:44px;width:123px;height:81px" role="img" aria-label="Photo of a shark in blue water"></div>
  <div class="photo ph-whale" style="left:156px;top:44px;width:123px;height:81px" role="img" aria-label="Photo of a whale shark close up"></div>
  <p class="body-text" style="left:23px;top:134px;width:123px"><b>Lorem Ipsum</b> is simply dummy text of the printing and typesetting industry. Lorem Ipsum has been the industry's standard dummy text ever since the 1500s.</p>
  <p class="body-text" style="left:156px;top:134px;width:123px"><b>Lorem Ipsum</b> is simply dummy text of the printing and typesetting industry. Lorem Ipsum has been the industry's standard dummy text ever since the 1500s.</p>
  <div class="footer">The Reefside Clinic presentation to: <span>Harbourview Marine Park</span></div>
  <div class="page-no">Page: 9</div>
</section>

<!-- 10 portfolio images -->
<section class="slide col-b row-5">
  <h2 class="title">PORTAFOLIO IMAGES</h2>
  <div class="subtitle">Lorem ipsum, giving information on its origins, as well as a random text here</div>
  <div class="brand">The Reefside Clinic<i class="dot"></i></div>
  <div class="photo ph-fish" style="left:23px;top:46px;width:114px;height:52px" role="img" aria-label="Photo of a clown triggerfish"></div>
  <div class="photo ph-discus" style="left:138px;top:46px;width:70px;height:52px" role="img" aria-label="Photo of discus fish"></div>
  <div class="photo ph-ray" style="left:209px;top:46px;width:70px;height:52px" role="img" aria-label="Photo of an eagle ray"></div>
  <div class="photo ph-coral" style="left:23px;top:99px;width:65px;height:46px" role="img" aria-label="Photo of a red coral fish"></div>
  <div class="photo ph-turtle" style="left:89px;top:99px;width:119px;height:46px" role="img" aria-label="Photo of a sea turtle over a reef"></div>
  <div class="photo ph-seaturtle" style="left:209px;top:99px;width:70px;height:46px" role="img" aria-label="Photo of a sea turtle resting"></div>
  <div class="footer">The Reefside Clinic presentation to: <span>Harbourview Marine Park</span></div>
  <div class="page-no">Page: 10</div>
</section>

<!-- 11 text with four images -->
<section class="slide col-a row-6">
  <div class="brand" style="left:23px;right:auto;top:25px">The Reefside Clinic<i class="dot"></i></div>
  <h2 class="big-title" style="top:47px;font-size:15px">TEXT WITH<br>FOUR<br>IMAGES</h2>
  <p class="body-text" style="left:25px;top:96px;width:97px"><b>Lorem Ipsum</b> is simply dummy text of the printing and typesetting industry. Lorem Ipsum has been the industry's standard dummy text ever since the 1500s, when an unknown printer took a galley of type and scrambled it to make a type specimen book.</p>
  <div class="hline" style="left:0;top:127px;width:134px"></div>
  <div class="photo ph-penguin" style="left:134px;top:0;width:62px;height:127px" role="img" aria-label="Photo of a penguin swimming underwater"></div>
  <div class="photo ph-fish" style="left:134px;top:129px;width:62px;height:41px" role="img" aria-label="Photo of a clown triggerfish"></div>
  <div class="photo ph-seaturtle" style="left:198px;top:0;width:63px;height:55px" role="img" aria-label="Photo of a sea turtle"></div>
  <div class="hline" style="left:261px;top:56px;width:35px"></div>
  <div class="photo ph-reef" style="left:198px;top:57px;width:63px;height:113px" role="img" aria-label="Photo of schooling reef fish"></div>
  <div class="footer">The Reefside Clinic presentation to: <span>Harbourview Marine Park</span></div>
  <div class="page-no">Page: 11</div>
</section>

<!-- 12 questions -->
<section class="slide col-b row-6">
  <svg class="abs" style="left:0;top:0" width="302" height="170" viewBox="0 0 302 170" role="img" aria-label="Diagonal stripes filled with underwater reef imagery">
    <defs>
      <linearGradient id="stripe" x1="0" y1="0" x2="0" y2="1">
        <stop offset="0" stop-color="#2b9be0"/><stop offset="1" stop-color="#1565b8"/>
      </linearGradient>
    </defs>
    <polygon points="160,10 168,10 100,170 92,170" fill="#1c5fb3"/>
    <polygon points="190,8 202,8 128,170 116,170" fill="url(#stripe)"/>
    <polygon points="212,4 226,4 146,170 132,170" fill="url(#stripe)"/>
    <polygon points="236,0 250,0 168,170 154,170" fill="#1e7fd0"/>
    <polygon points="258,0 268,0 190,140 180,140" fill="url(#stripe)"/>
    <polygon points="276,0 290,0 220,130 206,130" fill="#3a86c8"/>
    <polygon points="215,40 222,40 185,105 178,105" fill="#56b4e9"/>
  </svg>
  <div class="brand" style="left:23px;right:auto;top:25px">The Reefside Clinic<i class="dot"></i></div>
  <h2 class="big-title" style="top:53px;font-size:18px">QUESTIONS?</h2>
  <p class="body-text" style="left:23px;top:75px;width:120px;font-size:3px">Lorem Ipsum is simply dummy text of the printing and typesetting industry. Lorem Ipsum has been the industry's standard dummy text ever.</p>
</section>

</div>
</body>
</html>
```